Business card design needed

We are a boutique law firm within the Melbourne CBD.

You will need to upload our company logo which is to go on the left hand side of the business card - we then have a Legal Guild of Carrowmere logo to go perhaps on the bottom right hand side (color)

On the back we would like the website details

www.hartwellsolicitors.com.au - with a small logo
Updates

Thank you designers for all your great submissions.  Just going through the designs and we will choose one within the next couple of days.

Kind Regards
Hartwells Solicitors Pty Ltd

Industry/Entity Type

Boutique

Contact Information for Business Card

Dominic Hartwell
Principal
Level 6, 47 Penrose Street
Melbourne VIC Australia 3000
T+61 3 9555 0142 F+61 3 9555 0187
dominic@hartwellsolicitors.com.au
M 0491 570 156

```html
<!DOCTYPE html>
<html lang="en">
<head>
<meta charset="utf-8">
<title>Hartwells Solicitors – Business Card</title>
<link href="https://fonts.googleapis.com/css2?family=Arimo:wght@400;700&display=swap" rel="stylesheet">
<style>
  :root {
    --stage: #d9dbdb;
    --ink: #111111;
    --paper: #ffffff;
    --card-black: #0b0b0b;
    --ghost: #1c1c1c;
    --rule: #222222;
    --badge-blue: #3a8fd0;
    --badge-ring: #1d3f74;
    --muted: #333333;
  }
  * { box-sizing: border-box; margin: 0; padding: 0; }
  html, body { width: 1200px; height: 771px; overflow: hidden; }
  body {
    background: var(--stage);
    font-family: "Arimo", Arial, sans-serif;
    color: var(--ink);
    position: relative;
  }
  .card {
    position: absolute;
    top: 226px;
    width: 520px;
    height: 318px;
    box-shadow: 0 6px 18px rgba(0,0,0,.18);
  }
  /* Back */
  .card-back { left: 50px; background: var(--card-black); color: var(--paper); overflow: hidden; }
  .card-back .ghost-name {
    position: absolute; left: 150px; top: 170px;
    font-weight: 700; font-size: 64px; color: var(--ghost); letter-spacing: -1px;
  }
  .card-back .web {
    position: absolute; left: 0; right: 0; top: 144px; text-align: center;
    font-size: 21px; font-weight: 400; letter-spacing: .2px;
  }
  /* Front */
  .card-front { left: 630px; background: var(--paper); }
  .brand {
    position: absolute; left: 30px; top: 58px;
    display: flex; align-items: flex-end; gap: 8px;
  }
  .brand-mark { width: 44px; height: 44px; background: var(--ink); }
  .brand-name { font-weight: 700; font-size: 30px; line-height: 1; letter-spacing: -.5px; }
  .person { position: absolute; right: 28px; top: 72px; text-align: right; }
  .person-name { font-weight: 700; font-size: 20px; line-height: 1; }
  .person-title {
    font-size: 12px; margin-top: 3px; padding-top: 2px;
    border-top: 1px solid var(--rule); display: inline-block; padding-left: 14px;
  }
  .address-line {
    position: absolute; left: 30px; width: 300px; top: 124px;
    font-size: 12.5px; padding-bottom: 4px; border-bottom: 1px solid var(--rule);
    white-space: nowrap;
  }
  .contacts { position: absolute; left: 30px; top: 176px; list-style: none; }
  .contacts li {
    display: flex; align-items: center; gap: 8px;
    font-size: 13px; line-height: 1; height: 17px;
  }
  .contacts svg { width: 13px; height: 13px; flex: none; }
  .guild { position: absolute; right: 26px; top: 150px; width: 110px; text-align: center; }
  .guild-badge { display: block; margin: 0 auto 8px; }
  .guild-note { font-size: 6px; line-height: 1.25; color: var(--muted); text-align: left; }
</style>
</head>
<body>

<section class="card card-back" aria-label="Card back">
  <div class="ghost-name" aria-hidden="true">Hartwells</div>
  <p class="web">www.hartwellsolicitors.com.au</p>
</section>

<section class="card card-front" aria-label="Card front">
  <div class="brand">
    <span class="brand-mark" aria-hidden="true"></span>
    <span class="brand-name">Hartwells</span>
  </div>

  <div class="person">
    <div class="person-name">Dominic Hartwell</div>
    <div class="person-title">Principal</div>
  </div>

  <p class="address-line">Level 6, 47 Penrose Street Melbourne VIC Australia 3000</p>

  <ul class="contacts">
    <li>
      <svg viewBox="0 0 13 13" aria-hidden="true"><rect width="13" height="13" rx="2" fill="#111"/><path d="M3 7 L6.5 3.5 L10 7 V10 H3 Z" fill="#fff"/></svg>
      Level 6, 47 Penrose Street
    </li>
    <li>
      <svg viewBox="0 0 13 13" aria-hidden="true"><rect width="13" height="13" rx="2" fill="#111"/><rect x="4.5" y="2.5" width="4" height="8" rx=".8" fill="none" stroke="#fff" stroke-width="1"/></svg>
      0491 570 156
    </li>
    <li>
      <svg viewBox="0 0 13 13" aria-hidden="true"><rect width="13" height="13" rx="2" fill="#111"/><path d="M3.5 3 Q3 7 8 10 L10 8.5 L8.5 7 L7.5 8 Q5.5 6.8 5 5 L6 4 L4.5 2.5 Z" fill="#fff"/></svg>
      +61 3 9555 0142
    </li>
    <li>
      <svg viewBox="0 0 13 13" aria-hidden="true"><rect width="13" height="13" rx="2" fill="#111"/><rect x="3" y="5" width="7" height="4.5" fill="#fff"/><rect x="4.2" y="3" width="4.6" height="2.5" fill="#fff"/></svg>
      +61 3 9555 0187
    </li>
    <li>
      <svg viewBox="0 0 13 13" aria-hidden="true"><rect width="13" height="13" rx="2" fill="#111"/><rect x="2.5" y="4" width="8" height="5.5" fill="none" stroke="#fff" stroke-width="1"/><path d="M2.5 4 L6.5 7 L10.5 4" fill="none" stroke="#fff" stroke-width="1"/></svg>
      dominic@hartwellsolicitors.com.au
    </li>
  </ul>

  <div class="guild">
    <svg class="guild-badge" width="40" height="40" viewBox="0 0 40 40" role="img" aria-label="Legal Guild of Carrowmere accreditation badge">
      <circle cx="20" cy="20" r="19" fill="#fff" stroke="var(--badge-ring)" stroke-width="1.5"/>
      <circle cx="20" cy="20" r="11" fill="var(--badge-blue)"/>
    </svg>
    <p class="guild-note">Dominic Hartwell is an accredited specialist in commercial litigation recognised by the guild as a leader in the field</p>
  </div>
</section>

</body>
</html>
```